Informational Business Handout needs Company Information

We have this informational handout that we would like to start handing out to clients; however, the original designer failed to include any of our company contact information. Our main request is that you redesign this card with the appropriate contact information as listed below. We would like the information/content that is currently on the card to be on the new design as well. Feel free to take liberty with the rest of the card design, or not. Please see the card specifications and our company contact information below.

Card details: 7 x 5 inches (17.78 x 12.5 cm). Cardstock.

Company Contact Details:
Dorian Welkett, JD
TarnwickLaw, PLLC
482 E. Marlowe Ave, Ste. 310, St. George, UT 84770
hello@tarnwicklaw-mail.com
(435) 555-0147

```html
<!DOCTYPE html>
<html lang="en">
<head>
<meta charset="utf-8">
<title>TarnwickLaw Special Needs Trust Handouts</title>
<link rel="stylesheet" href="https://fonts.googleapis.com/css2?family=Montserrat:wght@400;500;600;800;900&display=swap">
<style>
  :root {
    --navy: #0d2f6b;
    --navy-deep: #0a2a63;
    --orange: #d44a26;
    --ink: #2f3340;
    --paper: #ffffff;
    --backdrop: #3a3a3a;
  }
  * { box-sizing: border-box; margin: 0; padding: 0; }
  html, body { width: 1200px; height: 1200px; overflow: hidden; }
  body {
    background: var(--backdrop);
    font-family: "Montserrat", sans-serif;
    position: relative;
  }
  .handout {
    position: absolute;
    left: 220px;
    width: 760px;
    height: 535px;
    background: var(--paper);
    overflow: hidden;
    box-shadow: 0 6px 18px rgba(0,0,0,0.45);
  }
  .handout--first { top: 48px; }
  .handout--third { top: 614px; }
  .handout__shapes { position: absolute; inset: 0; }
  .handout__content {
    position: absolute;
    color: var(--ink);
  }
  .handout--first .handout__content { left: 56px; top: 86px; width: 356px; }
  .handout--third .handout__content { left: 42px; top: 100px; width: 372px; }
  .headline {
    font-weight: 900;
    color: var(--navy);
    font-size: 19px;
    line-height: 1.22;
    text-transform: uppercase;
    letter-spacing: 0.1px;
  }
  .intro {
    font-size: 10.4px;
    line-height: 1.14;
    font-weight: 400;
    margin-top: 10px;
  }
  .checklist-title {
    font-weight: 900;
    color: var(--navy);
    font-size: 11px;
    text-transform: uppercase;
    margin-top: 14px;
  }
  .checklist { list-style: none; margin-top: 8px; }
  .checklist li {
    display: flex;
    gap: 10px;
    font-size: 11.6px;
    font-weight: 600;
    line-height: 1.04;
    margin-bottom: 7px;
  }
  .handout--third .checklist li { margin-bottom: 14px; }
  .checkbox {
    flex: none;
    width: 12px; height: 12px;
    border: 1.4px solid var(--ink);
    border-radius: 2px;
    margin-top: 1px;
  }
  .closing {
    font-size: 10.4px;
    line-height: 1.14;
    margin-top: 14px;
    width: 290px;
  }
  .handout--third .closing { margin-top: 16px; }
  .brand {
    position: absolute;
    left: 445px;
    top: 210px;
    width: 300px;
    display: flex;
    align-items: center;
    justify-content: center;
    gap: 10px;
  }
  .brand__mark {
    width: 12px; height: 12px;
    background: var(--orange);
  }
  .brand__name {
    font-weight: 600;
    font-size: 26px;
    letter-spacing: 3px;
    color: var(--navy);
    text-transform: uppercase;
  }
  .contact {
    position: absolute;
    left: 484px;
    top: 426px;
    color: #ffffff;
    font-size: 12.4px;
    line-height: 1.12;
    font-weight: 400;
    font-style: normal;
    white-space: nowrap;
  }
  .contact__name { margin-bottom: 8px; }
  .contact__row { display: flex; gap: 6px; margin-bottom: 5px; }
  .contact__row:last-child { margin-bottom: 0; }
  .contact__icon { flex: none; width: 12px; height: 14px; margin-top: 0; }
</style>
</head>
<body>

<article class="handout handout--first">
  <svg class="handout__shapes" viewBox="0 0 760 535" aria-hidden="true">
    <defs>
      <linearGradient id="cornerFade1" x1="0" y1="0.6" x2="1" y2="0">
        <stop offset="0" stop-color="#d44a26"/>
        <stop offset="0.45" stop-color="#b4452f"/>
        <stop offset="1" stop-color="#0d2f6b"/>
      </linearGradient>
    </defs>
    <polygon points="0,0 236,0 0,101" fill="url(#cornerFade1)"/>
    <polygon points="236,535 760,309 760,535" fill="var(--navy-deep)"/>
  </svg>
  <div class="handout__content">
    <h1 class="headline">Is a First-Party<br>Special Needs Trust<br>Right for You?</h1>
    <p class="intro">Do you have a recognized disability by the Social Security Administration that renders you unable to engage in any substantial gainful activity by reason of any medically determined physical or mental impairment which can be expected to result in death or which has lasted or can be expected to last for a continuous period of not less than twelve months?</p>
    <h2 class="checklist-title">Are you...</h2>
    <ul class="checklist">
      <li><span class="checkbox"></span>Under age 65?</li>
      <li><span class="checkbox"></span>Expecting settlement proceeds from the negligent actions of a third party?</li>
      <li><span class="checkbox"></span>Expecting an inheritance?</li>
      <li><span class="checkbox"></span>Currently receiving, or will be applying for Social Security income?</li>
      <li><span class="checkbox"></span>Currently receiving, or will be applying for Medicaid?</li>
      <li><span class="checkbox"></span>Wanting to maintain or qualify for Social Security Income and/or medicaid after being awarded your settlement or inheritance?</li>
    </ul>
    <p class="closing">If you have a recognized disability and you answered yes to any of these questions, you should contact our office to discuss whether a First-Party Special Needs Trust is right for you.</p>
  </div>
  <div class="brand"><span class="brand__mark"></span><span class="brand__name">TarnwickLaw</span></div>
  <address class="contact">
    <p class="contact__name">Dorian Welkett, JD | TarnwickLaw, PLLC</p>
    <p class="contact__row"><svg class="contact__icon" viewBox="0 0 12 14"><path d="M6 0.5a4.8 4.8 0 0 0-4.8 4.8C1.2 9 6 13.5 6 13.5s4.8-4.5 4.8-8.2A4.8 4.8 0 0 0 6 0.5zm0 6.8a2 2 0 1 1 0-4 2 2 0 0 1 0 4z" fill="var(--orange)"/></svg><span>482 E. Marlowe Ave,<br>Ste. 310, St. George, UT 84770</span></p>
    <p class="contact__row"><svg class="contact__icon" viewBox="0 0 12 14"><rect x="0.5" y="3.5" width="11" height="8" fill="var(--orange)"/><path d="M0.5 3.5L6 8l5.5-4.5" stroke="var(--navy-deep)" stroke-width="1" fill="none"/></svg><span>hello@tarnwicklaw-mail.com</span></p>
    <p class="contact__row"><svg class="contact__icon" viewBox="0 0 12 14"><path d="M2.5 1.5l2.2 2.7-1.2 1.6c.8 1.7 2 2.9 3.6 3.7l1.6-1.2 2.7 2.2-1.3 2C5.6 12.3 1.5 8.1 1 2.8z" fill="var(--orange)"/></svg><span>(435) 555-0147</span></p>
  </address>
</article>

<article class="handout handout--third">
  <svg class="handout__shapes" viewBox="0 0 760 535" aria-hidden="true">
    <defs>
      <linearGradient id="cornerFade2" x1="0" y1="0.6" x2="1" y2="0">
        <stop offset="0" stop-color="#d44a26"/>
        <stop offset="0.45" stop-color="#b4452f"/>
        <stop offset="1" stop-color="#0d2f6b"/>
      </linearGradient>
    </defs>
    <polygon points="0,0 236,0 0,101" fill="url(#cornerFade2)"/>
    <polygon points="236,535 760,309 760,535" fill="var(--navy-deep)"/>
  </svg>
  <div class="handout__content">
    <h1 class="headline">Is a Third-Party Supplemental<br>Needs Trust Necessary for<br>Your Estate Plan?</h1>
    <p class="intro">Will one of your intended beneficiaries have a recognized disability as determined by the Social Security Administration that renders the beneficiary unable to engage in any substantial gainful activity by reason of any medically determined physical or mental impairment which can be expected to result in death or which has lasted or can be expected to last for a continuous period of not less than twelve months?</p>
    <h2 class="checklist-title">Does the intended beneficiary...</h2>
    <ul class="checklist">
      <li><span class="checkbox"></span>Currently receive or will be applying for Social Security Income?</li>
      <li><span class="checkbox"></span>Currently receive, or plan to apply for Medicaid?</li>
      <li><span class="checkbox"></span>Want to maintain or qualify for Social Security Income and/or medicaid after benefitting from an inheritance?</li>
    </ul>
    <p class="closing">If you have an intended beneficiary with a recognized disability and you answered yes to any of these questions, you should contact our office to discuss whether a Third-Party Supplemental Needs Trust is right for your estate plan.</p>
  </div>
  <div class="brand"><span class="brand__mark"></span><span class="brand__name">TarnwickLaw</span></div>
  <address class="contact">
    <p class="contact__name">Dorian Welkett, JD | TarnwickLaw, PLLC</p>
    <p class="contact__row"><svg class="contact__icon" viewBox="0 0 12 14"><path d="M6 0.5a4.8 4.8 0 0 0-4.8 4.8C1.2 9 6 13.5 6 13.5s4.8-4.5 4.8-8.2A4.8 4.8 0 0 0 6 0.5zm0 6.8a2 2 0 1 1 0-4 2 2 0 0 1 0 4z" fill="var(--orange)"/></svg><span>482 E. Marlowe Ave,<br>Ste. 310, St. George, UT 84770</span></p>
    <p class="contact__row"><svg class="contact__icon" viewBox="0 0 12 14"><rect x="0.5" y="3.5" width="11" height="8" fill="var(--orange)"/><path d="M0.5 3.5L6 8l5.5-4.5" stroke="var(--navy-deep)" stroke-width="1" fill="none"/></svg><span>hello@tarnwicklaw-mail.com</span></p>
    <p class="contact__row"><svg class="contact__icon" viewBox="0 0 12 14"><path d="M2.5 1.5l2.2 2.7-1.2 1.6c.8 1.7 2 2.9 3.6 3.7l1.6-1.2 2.7 2.2-1.3 2C5.6 12.3 1.5 8.1 1 2.8z" fill="var(--orange)"/></svg><span>(435) 555-0147</span></p>
  </address>
</article>

</body>
</html>
```